Robotic Physical Therapy office needs a Grand Opening Flyer

We need a Grand Opening flyer design for a robotic physical therapy office named Stellar Motion Therapy. We would like it to have a clean, classy, upscale feeling that gives potential clients a V.I.P. feeling. We would like to use the colors black, gray, and yellow (logo will be uploaded).

Event: Thursday, June 1st, 2023 from 12pm-6pm
location: 58274 Harlow Ave, Bloomfield Hills, MI 48319

Industry/Entity Type

Physical therapy

Font styles to use
Script

Colors

Designer to choose colors to be used in the design.

Requirements
Nice to have
• More of a vip feel for the invite

```html
<!DOCTYPE html>
<html lang="en">
<head>
<meta charset="utf-8">
<title>Stellar Motion Therapy – Grand Opening Ceremony</title>
<link href="https://fonts.googleapis.com/css2?family=Montserrat:wght@500;600;700;800&family=Satisfy&display=swap" rel="stylesheet">
<style>
  :root{
    --stage:#c9c9c9;
    --ink:#1f1f1f;
    --white:#ffffff;
    --gold:#fdd03b;
    --amber-top:#fdc940;
    --amber-bottom:#ffa52d;
    --silver-light:#f4f4f4;
    --silver-mid:#bdbdbd;
    --silver-dark:#8a8a8a;
    --photo-a:#e9ecef;
    --photo-b:#9fb4c8;
  }
  html,body{margin:0;padding:0;}
  body{
    width:1200px;height:2263px;overflow:hidden;
    background:var(--stage);
    display:flex;align-items:center;justify-content:center;
  }
  .flyer{width:1120px;height:1583px;display:block;box-shadow:0 10px 30px rgba(0,0,0,.35);}
  .brand-name{font-family:'Montserrat',sans-serif;font-weight:700;fill:var(--white);}
  .headline{font-family:'Montserrat',sans-serif;font-weight:800;fill:var(--white);}
  .script{font-family:'Satisfy',cursive;fill:var(--gold);}
  .tagline{font-family:'Montserrat',sans-serif;font-weight:600;fill:var(--ink);}
  .chip-label{font-family:'Montserrat',sans-serif;font-weight:500;fill:var(--white);}
  .detail{font-family:'Montserrat',sans-serif;font-weight:800;fill:var(--ink);}
  .address{font-family:'Montserrat',sans-serif;font-weight:500;fill:var(--ink);}
</style>
</head>
<body>
<svg class="flyer" viewBox="0 0 1040 1470" xmlns="http://www.w3.org/2000/svg">
  <defs>
    <linearGradient id="amberFill" x1="0" y1="0" x2="0" y2="1">
      <stop offset="0" stop-color="var(--amber-top)"/>
      <stop offset="1" stop-color="var(--amber-bottom)"/>
    </linearGradient>
    <linearGradient id="silverBand" x1="0" y1="0" x2="0" y2="1">
      <stop offset="0" stop-color="var(--silver-dark)"/>
      <stop offset=".35" stop-color="var(--silver-light)"/>
      <stop offset=".7" stop-color="var(--silver-mid)"/>
      <stop offset="1" stop-color="var(--silver-dark)"/>
    </linearGradient>
    <linearGradient id="photoTone" x1="0" y1="0" x2="1" y2="1">
      <stop offset="0" stop-color="var(--photo-a)"/>
      <stop offset="1" stop-color="var(--photo-b)"/>
    </linearGradient>
  </defs>

  <!-- backgrounds -->
  <rect class="panel-dark" width="1040" height="1470" fill="var(--ink)"/>
  <path class="panel-amber" d="M0 955 Q520 935 1040 950 L1040 1470 L0 1470 Z" fill="url(#amberFill)"/>
  <path class="silver-band" d="M0 840 Q520 865 1040 840 L1040 955 Q520 935 0 960 Z" fill="url(#silverBand)"/>

  <!-- brand -->
  <g class="brand">
    <circle cx="392" cy="122" r="62" fill="none" stroke="var(--white)" stroke-width="8"/>
    <text class="brand-name" x="480" y="112" font-size="50">STELLAR MOTION</text>
    <text class="brand-name" x="480" y="170" font-size="50">THERAPY</text>
  </g>

  <!-- headline -->
  <text class="headline" x="520" y="345" font-size="118" text-anchor="middle">GRAND</text>
  <text class="headline" x="242" y="458" font-size="118" textLength="560" lengthAdjust="spacingAndGlyphs">OPENING</text>
  <text class="script" x="395" y="525" font-size="132">Ceremony</text>

  <!-- tagline pill -->
  <rect x="242" y="548" width="556" height="62" rx="31" fill="var(--gold)"/>
  <text class="tagline" x="520" y="591" font-size="36" text-anchor="middle">Robotic Physical Therapy</text>

  <!-- photo -->
  <circle cx="520" cy="885" r="243" fill="var(--white)"/>
  <circle cx="520" cy="885" r="228" fill="url(#photoTone)" role="img" aria-label="Photo of a therapist helping a patient seated in a robotic therapy machine"/>

  <!-- event -->
  <rect x="447" y="1147" width="145" height="44" rx="14" fill="var(--ink)"/>
  <text class="chip-label" x="520" y="1180" font-size="28" text-anchor="middle">EVENT</text>

  <g class="icon-calendar" fill="var(--ink)">
    <rect x="98" y="1220" width="30" height="28" rx="3"/>
    <rect x="102" y="1231" width="22" height="13" fill="var(--amber-top)"/>
    <rect x="105" y="1233" width="4" height="4"/><rect x="111" y="1233" width="4" height="4"/><rect x="117" y="1233" width="4" height="4"/>
    <rect x="105" y="1239" width="4" height="4"/><rect x="111" y="1239" width="4" height="4"/><rect x="117" y="1239" width="4" height="4"/>
  </g>
  <text class="detail" x="150" y="1250" font-size="40">JUNE 1ST, 2023</text>
  <text class="detail" x="150" y="1300" font-size="40">THURSDAY</text>

  <line x1="520" y1="1218" x2="520" y2="1302" stroke="var(--ink)" stroke-width="3"/>

  <g class="icon-clock" fill="none" stroke="var(--ink)" stroke-width="4">
    <circle cx="593" cy="1234" r="16"/>
    <path d="M593 1224 V1235 L600 1240"/>
  </g>
  <text class="detail" x="633" y="1250" font-size="40">FROM</text>
  <text class="detail" x="633" y="1300" font-size="40">12PM-6PM</text>

  <!-- location -->
  <rect x="423" y="1325" width="193" height="44" rx="14" fill="var(--ink)"/>
  <text class="chip-label" x="520" y="1358" font-size="28" text-anchor="middle">LOCATION</text>
  <text class="address" x="520" y="1421" font-size="30" text-anchor="middle">58274 Harlow Ave, Bloomfield Hills, MI 48319</text>
</svg>
</body>
</html>
```